Layout reusable planting plan

Requested, a reusable layout for planting schemes (for ponds, backyard and so on). It will be used throughout a online course about ecological garden design. The focus is on the layout, not the content, as I will fill that myself.

I’m an ecological landscape designer and teacher ecological architecture, wishing to share my knowledge by building a course. I build the course from scratch, course is under construction.

If I like the delivered layout and there’s a mutual match a long-term cooperation might be the result/more assignments will follow. I hope to find a creative wizard who can think along of creative solutions for infographics too, who can make beautiful visualisations, all in a professional style (pictures, graphs, tables and so on) for the rest of the course.

Requirements:
• It needs to consist (on one page) of a:
o Moodboard
o Planting plan (in 2D (create a pond with plants in it), with division into:
 For ponds:
• At the edge
• Floating plants and water lilies
• Submerged plants
o Table with information about the plants (suitable for about 20 plants), including a scroll bar with which you can tell which water depth the plant prefers)
o A flowering arch, with some extra info about plants (with the colors) and some visualisation of the seasons
o Companion planting table
o If you have a suggestion for a 3D design/impression, please help me out
o For inspiration, see included examples, but create something yourself, as it’s about the layout, not the content
• Use @ Example 1_Factsheet online course as the starting point/document in which to make the plan, but only use the top heading and footer, the rest needs to be adjusted and improved. It’s up to you how to present it (layout, colors, graphs, etc.)
• Layout reusable, as the course will contain multiple planting schemes for ponds and for the sake of a consistent style.
• Layout planting scheme itself fit with the style of the online course, see below for more information about the course
• Dimensions (layout) planting plan in line with that of the slides of the online course (it would be great if the planting plan also fit on a slide of the online course)
• Planting plan needs to be printable on A4 landscape format (and still readable)
• all text should be adaptable (for translation to my native language)
• Layout planting scheme contains (see starting document (@ Example 1_Factsheet online course):
o Name (for example: Planting plan pond)
o The logo (see attachment)
o copyright Verdant Institute (for example © Verdant Institute)
o name of website (www.verdantinstitute.nl)
o page number (1 of 1 if one page)
• Layout needs to be easily adaptable
• Delivery in InDesign and illustrator, delivered in layers

I included the layout / style of the course under construction, so that you know which colors, fonts, backgrounds and so on are used. I included some examples/slides of the online course too (for a better understanding).

Layout online course:
• Slide size 1080 x 1920 (px) or 28,57 x 50,8 centimeter
• Colour palet online course: dark blue (#002D46), light blue (#D9EFFF), blue (#35A7FF), earth tone (#F4D99F) and green (#11AB47) and light red/orange (#F3593C)
• Background color is mostly white or dark blue, sometimes the other colors.
• Background contains a pattern
• Text itself is mostly black or white (if background is dark blue), headers are many times green (#11AB47)
• Font titless are Baloo Bhaijaan 2 extra bold, font size titels varies between 54 and 88, font size headers is mostly 36
• Font headers are Baloo Bhaijaan 2 semibold, font size headers mostly 36
• Font reading text is poppins light regular, font size 20 (at title slides sometimes 24), spacing single

```html
<!DOCTYPE html>
<html lang="en">
<head>
<meta charset="utf-8">
<title>Planting Plan Pond – Verdant Institute</title>
<link href="https://fonts.googleapis.com/css2?family=Baloo+Bhaijaan+2:wght@600;800&family=Poppins:ital,wght@0,300;0,400;0,500;0,600;0,700;1,300;1,400&display=swap" rel="stylesheet">
<style>
:root{
  --navy:#0d2b45;
  --green:#2f9a3e;
  --green-br:#11ab47;
  --lime:#8cc63f;
  --blue:#35a7ff;
  --light-blue:#d9efff;
  --earth:#f4d99f;
  --red:#f3593c;
  --brown:#b5722c;
  --ink:#1b2530;
  --line:#d6dde3;
}
*{box-sizing:border-box;margin:0;padding:0}
html,body{width:1200px;height:825px;overflow:hidden;background:#fff}
body{font-family:"Poppins",sans-serif;color:var(--ink);position:relative}
.page{position:relative;width:1200px;height:825px;background:#fff;overflow:hidden}
.abs{position:absolute}

/* header */
.header{position:absolute;left:0;top:0;width:1200px;height:69px;background:var(--navy)}
.brand{position:absolute;left:0;top:0;width:196px;height:69px;background:#fff;border-radius:0 0 90px 0/0 0 69px 0;display:flex;align-items:center;gap:8px;padding-left:32px}
.brand-dot{width:28px;height:28px;border-radius:50%;background:var(--green-br)}
.brand-name{font-family:"Baloo Bhaijaan 2",sans-serif;font-weight:800;font-size:17px;line-height:1;color:var(--green-br)}
.title{position:absolute;left:270px;top:7px;font-family:"Baloo Bhaijaan 2",sans-serif;font-weight:800;font-size:32px;color:#fff;letter-spacing:.5px;line-height:1.1}
.title em{font-style:normal;font-weight:600;font-size:22px;color:var(--green-br);margin-left:10px}
.subtitle{position:absolute;left:271px;top:48px;font-size:12.5px;font-weight:300;color:#fff}
.feature{position:absolute;top:11px;width:100px;text-align:center;color:#fff;font-size:7.6px;line-height:1.25;letter-spacing:.4px;text-transform:uppercase}
.feature svg{display:block;margin:0 auto 5px;width:22px;height:22px}
.vsep{position:absolute;top:13px;width:1px;height:44px;background:rgba(255,255,255,.35)}

/* footer */
.footer{position:absolute;left:0;bottom:0;width:1200px;height:33px;background:var(--navy);color:#fff;font-size:9.5px;display:flex;align-items:center;justify-content:space-between;padding:0 52px 0 28px}
.footer .web{color:var(--green-br);font-size:11px;font-weight:500}

/* section titles */
.sec-title{position:absolute;font-size:11px;font-weight:600;color:var(--green);text-transform:uppercase;letter-spacing:.2px;line-height:14px}
.sec-title small{font-size:8px;text-transform:none;font-weight:400}
.rule-h{position:absolute;height:1px;background:var(--line)}
.rule-v{position:absolute;width:1px;background:var(--line)}

/* placeholders */
.ph{position:absolute;overflow:hidden}
.circle{border-radius:50%;border:2px solid #fff;box-shadow:0 1px 3px rgba(0,0,0,.18)}
.note{position:absolute;font-size:7.5px;font-style:italic;font-weight:300;color:#333}

/* pond legend */
.pond-legend{position:absolute;left:326px;top:311px;width:92px;height:196px;border:1px solid var(--line);border-radius:6px;background:#fff;padding:7px 5px}
.pl-item{position:relative;padding-left:20px;margin-bottom:9px}
.pl-item .mk{position:absolute;left:0;top:0}
.pl-item h4{font-size:6.3px;font-weight:600;color:var(--navy);text-transform:uppercase;line-height:1.2}
.pl-item p{font-size:6.2px;line-height:1.35;color:#333;margin-top:3px}
.mk{display:inline-flex;align-items:center;justify-content:center;width:14px;height:14px;border-radius:50%;color:#fff;font-size:8px;font-weight:600;border:1.5px solid #fff}
.mk.g{background:var(--lime)}.mk.p{background:#8a4fbf}.mk.t{background:#3fb59a}
.mk.big{width:20px;height:20px;font-size:11px;box-shadow:0 1px 3px rgba(0,0,0,.3);position:absolute}

/* plant table */
.ptable{position:absolute;left:445px;top:115px;width:716px;border-collapse:collapse;table-layout:fixed;font-size:7.6px}
.ptable th{height:19px;font-weight:600;font-size:7.4px;border:1px solid #bfc8cf;background:#fff;color:#111;padding:0 3px;line-height:17px}
.ptable th small{font-weight:300;font-size:5.5px}
.ptable tbody tr{height:14.2px}
.ptable td{height:14.2px;line-height:12px;border-bottom:1px solid #e6eaee;border-left:1px solid #bfc8cf;border-right:1px solid #bfc8cf;padding:0 4px;white-space:nowrap;overflow:hidden;position:relative}
.ptable tr.gb td{border-bottom:1px solid #9fb0bd}
.ptable td.c{text-align:center}
.ptable td.sci{font-style:italic;font-weight:300}
.n,.z{display:inline-flex;align-items:center;justify-content:center;width:9px;height:9px;border-radius:50%;color:#fff;font-size:5.6px;line-height:1;font-weight:600;vertical-align:middle}
.n.g,.z.g{background:var(--green)}
.n.r{background:var(--red)}
.n.b,.z.b{background:var(--blue)}
.n.o,.z.o{background:var(--brown)}
.z.p{background:#8a4fbf}
.dp .tr{position:absolute;top:4.5px;height:5px;left:var(--t);right:4%;border-radius:3px;background:#e3e7eb}
.dp .fi{position:absolute;top:4.5px;height:5px;left:var(--l);width:var(--w);border-radius:3px;background:linear-gradient(90deg,#2a6fc9,#5aa9f0)}
.scale{display:flex;justify-content:space-between;padding:0 8px 0 2px;font-weight:400;font-size:6px;line-height:14px}
.scale-line{position:absolute;left:8px;right:10px;bottom:2px;height:2px;background:linear-gradient(90deg,#9fc6ef,#2a6fc9)}
.fl{padding:0!important}
.months,.fl span{display:grid;grid-template-columns:repeat(12,1fr);align-items:center;justify-items:center}
.months b{font-weight:400;font-size:6px;border-right:1px solid #e3e7eb;width:100%;text-align:center;line-height:17px}
.fl span{height:13px;background:linear-gradient(90deg,transparent calc(100% - 1px),#eef1f4 0) 0 0/8.333% 100%}
.fl i{width:5px;height:5px;border-radius:50%}
.fl i.g{background:#4ea42f}.fl i.l{background:#8cc63f}.fl i.y{background:#f2c417}
.fl i.o{background:#f39a1e}.fl i.p{background:#e0457b}.fl i.v{background:#7b4fb0}.fl i.b{background:#2f86e0}
.nt svg{width:8px;height:8px;margin-right:2px;vertical-align:middle}
.tbl-label{position:absolute;font-size:7.4px;font-weight:600;color:#111;line-height:10px}
.tbl-label small{font-weight:300;font-size:5.5px}
.scroll{position:absolute;left:1170px;top:152px;width:5px;height:266px;border-radius:3px;background:#e8edf1}
.scroll::after{content:"";position:absolute;left:0;top:8px;width:5px;height:55px;border-radius:3px;background:#7ea3c8}

/* arch */
.arch{position:absolute;left:452px;top:442px}
.arch-legend{position:absolute;left:574px;top:560px;font-size:6.6px;line-height:11px}
.arch-legend div{display:flex;align-items:center;gap:5px}
.arch-legend i{width:6px;height:6px;border-radius:50%;display:inline-block}
.seasons{position:absolute;left:431px;top:622px;width:375px;display:grid;grid-template-columns:repeat(4,1fr);gap:2px}
.season{height:61px;border-radius:3px;overflow:hidden;border:1px solid #cfd6dc}
.season h5{height:15px;line-height:15px;text-align:center;color:#fff;font-size:8.5px;font-weight:600;letter-spacing:.4px}
.season p{height:46px;font-size:6.3px;line-height:10.5px;color:#fff;text-align:center;padding-top:6px;text-shadow:0 0 3px rgba(0,0,0,.6)}
.s1 h5{background:#6fb24a}.s1 p{background:linear-gradient(160deg,#9bc77a,#4f7f3c)}
.s2 h5{background:#3aa58a}.s2 p{background:linear-gradient(160deg,#7cb57a,#4c7b5b)}
.s3 h5{background:#f0a437}.s3 p{background:linear-gradient(160deg,#d9a25c,#8b5a2c)}
.s4 h5{background:#2e5d86}.s4 p{background:linear-gradient(160deg,#a9c4da,#4f7190)}

/* companion */
.ctable{position:absolute;left:825px;top:468px;width:358px;border-collapse:collapse;table-layout:fixed;font-size:7.8px}
.ctable th{height:23px;font-size:6.2px;font-weight:400;text-align:left;vertical-align:middle;border-bottom:1px solid #bfc8cf}
.ctable th.plant{font-size:8px;font-weight:600;vertical-align:bottom;padding:0 0 3px 4px}
.ctable th .hd{display:flex;align-items:center;gap:3px;line-height:1.15}
.ctable th svg{width:14px;height:14px;flex:none}
.ctable td{height:16.8px;border:1px solid #dfe4e8;text-align:center}
.ctable td:first-child{text-align:left;padding-left:4px;border-left:none}
.dot{display:inline-block;width:8px;height:8px;border-radius:50%;vertical-align:middle}
.d-g{background:#2f9a3e}.d-b{background:#5da6dc}.d-o{background:#f4a623}.d-ol{background:#f2b965}
.d-br{background:#b8742c}.d-brl{background:#c9965a}.d-r{background:#f0503a}.d-rl{background:#f3d3a4}.d-p{background:#6b2fa8}.d-rp{background:#e36a5a}

/* how-to */
.howto{position:absolute;left:15px;top:698px;width:190px;height:64px;background:#eaf4fc;border-radius:8px 30px 30px 8px;padding:7px 10px}
.howto h3{font-size:9.5px;font-weight:600;color:var(--navy);letter-spacing:.2px;line-height:12px}
.howto p{font-size:6.6px;line-height:1.45;margin-top:3px}
.step{position:absolute;top:714px;display:flex;align-items:center;gap:8px;font-size:7.2px;line-height:1.55;color:#333}
.step svg{width:24px;height:24px;flex:none}
.legend{position:absolute;left:800px;top:698px;width:383px;height:64px;border:1px solid var(--line);border-radius:8px;padding:6px 12px}
.legend h3{font-size:7.6px;font-weight:600;color:var(--navy)}
.legend-row{display:flex;justify-content:space-between;margin-top:9px}
.legend-row div{display:flex;align-items:center;gap:5px;font-size:6px;line-height:1.3}
.legend-row svg{width:15px;height:15px;flex:none}
</style>
</head>
<body>
<svg width="0" height="0" style="position:absolute">
  <defs>
    <symbol id="i-bee" viewBox="0 0 10 10"><ellipse cx="5" cy="5.5" rx="3.4" ry="2.8" fill="#f2c417"/><rect x="4" y="2.8" width="1.2" height="5.4" fill="#3a2d12"/><ellipse cx="3.5" cy="2.6" rx="1.6" ry="1.1" fill="#bfdcf3"/><ellipse cx="6.5" cy="2.6" rx="1.6" ry="1.1" fill="#bfdcf3"/></symbol>
    <symbol id="i-drop" viewBox="0 0 10 10"><path d="M5 .8C3.4 3.4 2 5 2 6.6a3 3 0 0 0 6 0C8 5 6.6 3.4 5 .8z" fill="#3f8fdc"/></symbol>
    <symbol id="i-leaf" viewBox="0 0 10 10"><path d="M1.5 8.5C1.5 4 4.5 1.5 8.7 1.3 8.5 5.5 6 8.5 1.5 8.5z" fill="#3e9b3a"/><path d="M1.5 8.5 6 4" stroke="#fff" stroke-width=".6"/></symbol>
    <symbol id="i-bird" viewBox="0 0 10 10"><path d="M1 5.5 4 4.2 5.2 1.5 6.3 4.3 9 5.2 6 6.3 4.6 8.8 4 6.3z" fill="#1f3f5f"/></symbol>
    <symbol id="i-frog" viewBox="0 0 10 10"><ellipse cx="5" cy="6" rx="3.6" ry="2.6" fill="#5fae3c"/><circle cx="3.3" cy="3.4" r="1.2" fill="#5fae3c"/><circle cx="6.7" cy="3.4" r="1.2" fill="#5fae3c"/></symbol>
    <symbol id="i-shade" viewBox="0 0 10 10"><path d="M1 5a4 4 0 0 1 8 0z" fill="#1b2530"/><path d="M5 5v3.5" stroke="#1b2530" stroke-width=".8"/></symbol>
    <symbol id="i-home" viewBox="0 0 10 10"><path d="M1 5 5 1.5 9 5v4H1z" fill="#1b2530"/><rect x="4" y="6" width="2" height="3" fill="#fff"/></symbol>
    <symbol id="i-grass" viewBox="0 0 10 10"><path d="M5 9V2M5 9 2 3M5 9l3-6M5 9 1 6M5 9l4-3" stroke="#3e9b3a" stroke-width=".8" fill="none"/></symbol>
  </defs>
</svg>

<div class="page">

  <!-- Header -->
  <header class="header">
    <div class="brand"><span class="brand-dot"></span><span class="brand-name">Verdant Institute</span></div>
    <h1 class="title">PLANTING PLAN POND<em>(Example)</em></h1>
    <p class="subtitle">A reusable template for ecological planting schemes</p>

    <div class="feature" style="left:737px">
      <svg viewBox="0 0 24 24"><path d="M12 3c-2 4-6 6-6 10a6 6 0 0 0 12 0c0-4-4-6-6-10z" fill="#9fd0f5"/><path d="M3 18c3 2 6 2 9 0s6-2 9 0" stroke="#fff" stroke-width="1.5" fill="none"/></svg>
      Supports<br>wildlife
    </div>
    <div class="vsep" style="left:836px"></div>
    <div class="feature" style="left:834px">
      <svg viewBox="0 0 24 24"><path d="M12 2C9 7 6 10 6 14a6 6 0 0 0 12 0c0-4-3-7-6-12z" fill="#d9efff"/><path d="M9 15a3 3 0 0 0 3 3" stroke="#35a7ff" stroke-width="1.5" fill="none"/></svg>
      Improves<br>water quality
    </div>
    <div class="vsep" style="left:940px"></div>
    <div class="feature" style="left:944px">
      <svg viewBox="0 0 24 24" fill="none" stroke="#fff" stroke-width="1.3"><circle cx="12" cy="12" r="2.5"/><path d="M12 2v5M12 17v5M2 12h5M17 12h5M5 5l3.5 3.5M15.5 15.5 19 19M19 5l-3.5 3.5M8.5 15.5 5 19"/></svg>
      Enhances<br>biodiversity
    </div>
    <div class="vsep" style="left:1055px"></div>
    <div class="feature" style="left:1046px">
      <svg viewBox="0 0 24 24" fill="none" stroke="#fff" stroke-width="1.4"><circle cx="12" cy="10" r="7"/><path d="M12 17v5M9 9l3 3 3-3"/></svg>
      Climate<br>resilient
    </div>
  </header>

  <!-- dividers -->
  <div class="rule-v" style="left:427px;top:85px;height:605px"></div>
  <div class="rule-h" style="left:18px;top:292px;width:400px"></div>
  <div class="rule-h" style="left:18px;top:516px;width:400px"></div>
  <div class="rule-h" style="left:437px;top:434px;width:748px"></div>
  <div class="rule-v" style="left:818px;top:442px;height:250px"></div>

  <!-- 1. Moodboard -->
  <h2 class="sec-title" style="left:31px;top:88px">1. Moodboard &amp; Inspiration</h2>
  <div class="ph" role="img" aria-label="Pond landscape photo with reeds, flowering banks and trees" style="left:33px;top:187px;width:186px;height:90px;border-radius:46px 60px 30px 20px;background:linear-gradient(180deg,#b9d7e6 0%,#6f9a4c 45%,#3f6a33 75%,#6b8f9c 100%)"></div>
  <div class="ph circle" role="img" aria-label="Pink flowering marsh plant" style="left:34px;top:160px;width:62px;height:62px;background:radial-gradient(circle,#d9a6b8,#6d7a46)"></div>
  <div class="ph circle" role="img" aria-label="Purple loosestrife flower spikes" style="left:92px;top:111px;width:70px;height:70px;background:radial-gradient(circle,#b18ad0,#5c7a3c)"></div>
  <div class="ph circle" role="img" aria-label="Frog resting on a leaf" style="left:170px;top:113px;width:62px;height:62px;background:radial-gradient(circle,#9cc05a,#3f6a2a)"></div>
  <div class="ph circle" role="img" aria-label="Yellow flag iris flower" style="left:240px;top:135px;width:60px;height:60px;background:radial-gradient(circle,#f2d43f,#3e5a26)"></div>
  <div class="ph circle" role="img" aria-label="Pink flower cluster" style="left:326px;top:92px;width:56px;height:56px;background:radial-gradient(circle,#e9b7c9,#5d8a3a)"></div>
  <div class="ph circle" role="img" aria-label="Dragonfly resting on a stem" style="left:296px;top:138px;width:82px;height:82px;background:radial-gradient(circle,#e2ecf0,#9cb8c4)"></div>
  <div class="ph circle" role="img" aria-label="Water lily pads on a pond" style="left:217px;top:196px;width:90px;height:90px;background:radial-gradient(circle,#7fae4a,#2f5a3a)"></div>
  <div class="ph circle" role="img" aria-label="White water lily flower" style="left:289px;top:232px;width:54px;height:54px;background:radial-gradient(circle,#ffffff 20%,#a7c3a0 60%,#3e6a4a)"></div>
  <div class="ph circle" role="img" aria-label="Tall grasses at the water's edge" style="left:346px;top:216px;width:66px;height:66px;background:radial-gradient(circle,#a8c96a,#4f7a32)"></div>
  <span class="note" style="left:33px;top:124px;transform:rotate(-10deg)">Wildlife habitat</span>
  <span class="note" style="left:250px;top:112px;transform:rotate(-12deg)">Seasonal interest</span>
  <span class="note" style="left:388px;top:172px;transform:rotate(-8deg);width:36px;line-height:1.2">Natural balance</span>

  <!-- 2. Planting plan -->
  <h2 class="sec-title" style="left:29px;top:298px">2. Pond Planting Plan <small>(Top View)</small></h2>
  <svg class="abs" style="left:303px;top:318px" width="10" height="14" viewBox="0 0 10 14"><text x="5" y="5" font-size="6" text-anchor="middle" font-family="Poppins,sans-serif" font-weight="600">N</text><path d="M5 6 2 13 5 11 8 13z" fill="#333"/></svg>
  <div class="ph" role="img" aria-label="Top view of a pond with planted edges, floating lilies and submerged plants" style="left:25px;top:316px;width:292px;height:192px;border-radius:48% 52% 45% 55%/50% 45% 55% 50%;background:radial-gradient(ellipse at 55% 55%,#4fa4b8 0%,#3f8ea6 35%,#6f9a4c 62%,#4f7a34 80%,#a7a08a 100%)"></div>
  <span class="mk big g" style="left:58px;top:342px">1</span>
  <span class="mk big p" style="left:152px;top:362px">2</span>
  <span class="mk big t" style="left:168px;top:399px">3</span>

  <div class="pond-legend">
    <div class="pl-item"><span class="mk g">1</span><h4>At the edge</h4><p>Moist soil &amp;<br>shallow water<br>0 – 20 cm</p></div>
    <div class="pl-item"><span class="mk p">2</span><h4>Floating plants &amp; water lilies</h4><p>Floating on the<br>water surface<br>0 – 60 cm</p></div>
    <div class="pl-item"><span class="mk t">3</span><h4>Submerged plants</h4><p>Fully submerged<br>(oxygenators)<br>30 – 120 cm+</p></div>
    <div class="pl-item"><svg class="mk" viewBox="0 0 14 14" style="border:none"><ellipse cx="6" cy="9" rx="5" ry="3.5" fill="#b7ab97"/><ellipse cx="9" cy="6" rx="4" ry="3" fill="#d2c8b6"/></svg><h4>Rock / wood</h4><p>Habitat &amp; shelter</p></div>
  </div>

  <!-- 3. 3D impression -->
  <h2 class="sec-title" style="left:29px;top:522px">3. 3D Impression <small>(Perspective View)</small></h2>
  <div class="ph" role="img" aria-label="Perspective cross-section of a planted pond with flowering edges and fish below the surface" style="left:28px;top:540px;width:392px;height:150px;border-radius:14px 14px 60px 60px;background:linear-gradient(180deg,#fff 0%,#b68fd1 12%,#7fae4a 30%,#5fb0c4 48%,#3f8ea6 68%,#6f5a3e 88%,#fff 100%)"></div>

  <!-- 4. Plant information table -->
  <h2 class="sec-title" style="left:449px;top:88px">4. Plant Information Table</h2>
  <span class="tbl-label" style="left:790px;top:104px">WATER DEPTH <small>(cm)</small></span>
  <span class="tbl-label" style="left:988px;top:104px">Flowers</span>
  <table class="ptable">
    <colgroup><col style="width:23px"><col style="width:97px"><col style="width:112px"><col style="width:29px"><col style="width:48px"><col style="width:177px"><col style="width:166px"><col style="width:64px"></colgroup>
    <thead>
      <tr>
        <th>No.</th><th>Plant name <small>(edit)</small></th><th>Scientific name <small>(edit)</small></th><th>Zone</th><th>Height <small>(cm)</small></th>
        <th style="position:relative;padding:0"><div class="scale"><span>-150</span><span>-100</span><span>-50</span><span>0</span><span>50</span><span>100</span><span>150+</span></div><div class="scale-line"></div></th>
        <th style="padding:0"><div class="months"><b>1</b><b>2</b><b>3</b><b>4</b><b>5</b><b>6</b><b>7</b><b>8</b><b>9</b><b>10</b><b>11</b><b>12</b></div></th>
        <th>Notes <small>(edit)</small></th>
      </tr>
    </thead>
    <tbody>
      <tr><td class="c"><b class="n g">1</b></td><td>Marsh Marigold</td><td class="sci">Caltha palustris</td><td class="c"><b class="z g">1</b></td><td class="c">30–50</td><td class="dp"><span class="tr" style="--t:21%"></span><span class="fi" style="--l:23%;--w:44%"></span></td><td class="fl"><span><i class="g"></i><i class="g"></i><i class="g"></i><i class="g"></i><i class="g"></i><i class="g"></i><i class="l"></i><i class="g"></i><i></i><i></i><i></i><i></i></span></td><td class="nt"><svg><use href="#i-bee"/></svg><svg><use href="#i-frog"/></svg><svg><use href="#i-drop"/></svg><svg><use href="#i-leaf"/></svg></td></tr>
      <tr><td class="c"><b class="n g">2</b></td><td>Yellow Flag Iris</td><td class="sci">Iris pseudacorus</td><td class="c"><b class="z g">1</b></td><td class="c">60–100</td><td class="dp"><span class="tr" style="--t:43%"></span><span class="fi" style="--l:46%;--w:33%"></span></td><td class="fl"><span><i class="g"></i><i class="g"></i><i class="g"></i><i class="g"></i><i class="y"></i><i class="y"></i><i></i><i></i><i></i><i></i><i></i><i></i></span></td><td class="nt"><svg><use href="#i-bird"/></svg><svg><use href="#i-drop"/></svg></td></tr>
      <tr><td class="c"><b class="n g">3</b></td><td>Bogbean</td><td class="sci">Menyanthes trifoliata</td><td class="c"><b class="z g">1</b></td><td class="c">20–30</td><td class="dp"><span class="tr" style="--t:32%"></span><span class="fi" style="--l:32%;--w:20%"></span></td><td class="fl"><span><i class="g"></i><i class="y"></i><i class="y"></i><i></i><i></i><i></i><i></i><i></i><i></i><i></i><i></i><i></i></span></td><td class="nt"><svg><use href="#i-bee"/></svg><svg><use href="#i-drop"/></svg></td></tr>
      <tr><td class="c"><b class="n g">4</b></td><td>Water Mint</td><td class="sci">Mentha aquatica</td><td class="c"><b class="z g">1</b></td><td class="c">30–80</td><td class="dp"><span class="tr" style="--t:43%"></span><span class="fi" style="--l:48%;--w:24%"></span></td><td class="fl"><span><i class="g"></i><i class="o"></i><i class="o"></i><i></i><i></i><i></i><i></i><i></i><i></i><i></i><i></i><i></i></span></td><td class="nt"><svg><use href="#i-drop"/></svg><svg><use href="#i-leaf"/></svg></td></tr>
      <tr><td class="c"><b class="n g">5</b></td><td>Purple Loosestrife</td><td class="sci">Lythrum salicaria</td><td class="c"><b class="z g">1</b></td><td class="c">80–150</td><td class="dp"><span class="tr" style="--t:43%"></span><span class="fi" style="--l:52%;--w:29%"></span></td><td class="fl"><span><i></i><i></i><i class="p"></i><i class="p"></i><i class="p"></i><i class="p"></i><i class="p"></i><i></i><i></i><i></i><i></i><i></i></span></td><td class="nt"><svg><use href="#i-drop"/></svg><svg><use href="#i-leaf"/></svg></td></tr>
      <tr><td class="c"><b class="n g">6</b></td><td>Sweet Flag</td><td class="sci">Acorus calamus</td><td class="c"><b class="z g">1</b></td><td class="c">60–120</td><td class="dp"><span class="tr" style="--t:43%"></span><span class="fi" style="--l:48%;--w:24%"></span></td><td class="fl"><span><i></i><i class="v"></i><i class="v"></i><i class="v"></i><i class="v"></i><i class="v"></i><i class="v"></i><i class="v"></i><i class="v"></i><i></i><i></i><i></i></span></td><td class="nt"><svg><use href="#i-bee"/></svg><svg><use href="#i-drop"/></svg></td></tr>
      <tr class="gb"><td class="c"><b class="n g">7</b></td><td>Water Plantain</td><td class="sci">Alisma plantago-aquatica</td><td class="c"><b class="z g">1</b></td><td class="c">40–80</td><td class="dp"><span class="tr" style="--t:37%"></span><span class="fi" style="--l:37%;--w:18%"></span></td><td class="fl"><span><i class="v"></i><i class="v"></i><i class="v"></i><i class="v"></i><i class="v"></i><i></i><i></i><i></i><i></i><i></i><i></i><i></i></span></td><td class="nt"><svg><use href="#i-bee"/></svg><svg><use href="#i-drop"/></svg><svg><use href="#i-leaf"/></svg></td></tr>
      <tr><td class="c"><b class="n r">8</b></td><td>Water Lily</td><td class="sci">Nymphaea alba</td><td class="c"><b class="z p">2</b></td><td class="c">–</td><td class="dp"><span class="tr" style="--t:6%"></span><span class="fi" style="--l:12%;--w:44%"></span></td><td class="fl"><span><i></i><i></i><i class="l"></i><i class="l"></i><i class="l"></i><i class="l"></i><i class="y"></i><i class="o"></i><i></i><i></i><i></i><i></i></span></td><td class="nt"><svg><use href="#i-bee"/></svg><svg><use href="#i-drop"/></svg><svg><use href="#i-frog"/></svg></td></tr>
      <tr><td class="c"><b class="n r">9</b></td><td>Yellow Water Lily</td><td class="sci">Nuphar lutea</td><td class="c"><b class="z p">2</b></td><td class="c">–</td><td class="dp"><span class="tr" style="--t:43%"></span><span class="fi" style="--l:46%;--w:13%"></span></td><td class="fl"><span><i></i><i></i><i></i><i class="o"></i><i class="o"></i><i class="y"></i><i class="o"></i><i class="o"></i><i class="l"></i><i class="l"></i><i></i><i></i></span></td><td class="nt"><svg><use href="#i-bee"/></svg><svg><use href="#i-drop"/></svg></td></tr>
      <tr><td class="c"><b class="n r">10</b></td><td>Frogbit</td><td class="sci">Hydrocharis morsus-ranae</td><td class="c"><b class="z p">2</b></td><td class="c">–</td><td class="dp"><span class="tr" style="--t:6%"></span><span class="fi" style="--l:15%;--w:38%"></span></td><td class="fl"><span><i></i><i></i><i class="l"></i><i class="l"></i><i class="l"></i><i class="l"></i><i class="l"></i><i class="o"></i><i></i><i></i><i></i><i></i></span></td><td class="nt"><svg><use href="#i-bee"/></svg><svg><use href="#i-drop"/></svg></td></tr>
      <tr class="gb"><td class="c"><b class="n r">11</b></td><td>Floating Heart</td><td class="sci">Nymphoides peltata</td><td class="c"><b class="z p">2</b></td><td class="c">–</td><td class="dp"><span class="tr" style="--t:28%"></span><span class="fi" style="--l:28%;--w:38%"></span></td><td class="fl"><span><i></i><i></i><i></i><i></i><i></i><i class="l"></i><i class="l"></i><i class="l"></i><i class="l"></i><i class="l"></i><i></i><i></i></span></td><td class="nt"><svg><use href="#i-bee"/></svg><svg><use href="#i-drop"/></svg><svg><use href="#i-drop"/></svg><svg><use href="#i-frog"/></svg></td></tr>
      <tr><td class="c"><b class="n b">12</b></td><td>Hornwort</td><td class="sci">Ceratophyllum demersum</td><td class="c"><b class="z b">3</b></td><td class="c">–</td><td class="dp"><span class="tr" style="--t:15%"></span><span class="fi" style="--l:17%;--w:51%"></span></td><td class="fl"><span><i></i><i></i><i class="p"></i><i class="p"></i><i class="p"></i><i class="p"></i><i></i><i></i><i></i><i></i><i></i><i></i></span></td><td class="nt"><svg><use href="#i-bird"/></svg><svg><use href="#i-frog"/></svg></td></tr>
      <tr><td class="c"><b class="n b">13</b></td><td>Water Milfoil</td><td class="sci">Myriophyllum spicatum</td><td class="c"><b class="z b">3</b></td><td class="c">–</td><td class="dp"><span class="tr" style="--t:26%"></span><span class="fi" style="--l:28%;--w:35%"></span></td><td class="fl"><span><i></i><i class="b"></i><i></i><i class="b"></i><i></i><i></i><i class="b"></i><i class="b"></i><i class="b"></i><i class="b"></i><i></i><i></i></span></td><td class="nt"><svg><use href="#i-drop"/></svg><svg><use href="#i-drop"/></svg><svg><use href="#i-frog"/></svg></td></tr>
      <tr><td class="c"><b class="n b">14</b></td><td>Pondweed</td><td class="sci">Potamogeton natans</td><td class="c"><b class="z b">3</b></td><td class="c">–</td><td class="dp"><span class="tr" style="--t:37%"></span><span class="fi" style="--l:40%;--w:27%"></span></td><td class="fl"><span><i></i><i class="b"></i><i></i><i class="b"></i><i class="b"></i><i class="b"></i><i class="b"></i><i></i><i></i><i></i><i></i><i></i></span></td><td class="nt"><svg><use href="#i-bee"/></svg><svg><use href="#i-drop"/></svg><svg><use href="#i-frog"/></svg></td></tr>
      <tr><td class="c"><b class="n b">15</b></td><td>Canadian Pondweed</td><td class="sci">Elodea canadensis</td><td class="c"><b class="z b">3</b></td><td class="c">–</td><td class="dp"><span class="tr" style="--t:37%"></span><span class="fi" style="--l:40%;--w:22%"></span></td><td class="fl"><span><i></i><i></i><i class="v"></i><i class="v"></i><i class="v"></i><i class="v"></i><i class="v"></i><i></i><i></i><i></i><i></i><i></i></span></td><td class="nt"><svg><use href="#i-bee"/></svg><svg><use href="#i-drop"/></svg><svg><use href="#i-frog"/></svg></td></tr>
      <tr class="gb"><td class="c"><b class="n b">16</b></td><td>Curly Pondweed</td><td class="sci">Potamogeton crispus</td><td class="c"><b class="z b">3</b></td><td class="c">–</td><td class="dp"><span class="tr" style="--t:37%"></span><span class="fi" style="--l:40%;--w:24%"></span></td><td class="fl"><span><i></i><i></i><i class="v"></i><i class="v"></i><i class="v"></i><i class="v"></i><i class="v"></i><i class="v"></i><i class="v"></i><i></i><i></i><i></i></span></td><td class="nt"><svg><use href="#i-drop"/></svg><svg><use href="#i-frog"/></svg><svg><use href="#i-drop"/></svg></td></tr>
      <tr><td class="c"><b class="n o">17</b></td><td>Soft Rush</td><td class="sci">Juncus effusus</td><td class="c"><b class="z o">1</b></td><td class="c">30–90</td><td class="dp"><span class="tr" style="--t:28%"></span><span class="fi" style="--l:33%;--w:20%"></span></td><td class="fl"><span><i class="g"></i><i class="g"></i><i class="g"></i><i class="l"></i><i class="g"></i><i class="l"></i><i></i><i></i><i></i><i></i><i></i><i></i></span></td><td class="nt"><svg><use href="#i-bird"/></svg><svg><use href="#i-drop"/></svg><svg><use href="#i-frog"/></svg></td></tr>
      <tr><td class="c"><b class="n o">18</b></td><td>Umbrella Sedge</td><td class="sci">Cyperus alternifolius</td><td class="c"><b class="z o">1</b></td><td class="c">60–120</td><td class="dp"><span class="tr" style="--t:43%"></span><span class="fi" style="--l:46%;--w:22%"></span></td><td class="fl"><span><i class="l"></i><i class="l"></i><i class="l"></i><i></i><i class="o"></i><i class="o"></i><i class="l"></i><i></i><i></i><i></i><i></i><i></i></span></td><td class="nt"><svg><use href="#i-bee"/></svg><svg><use href="#i-drop"/></svg></td></tr>
      <tr><td class="c"><b class="n o">19</b></td><td>Common Reed</td><td class="sci">Phragmites australis</td><td class="c"><b class="z o">1</b></td><td class="c">100–250</td><td class="dp"><span class="tr" style="--t:37%"></span><span class="fi" style="--l:40%;--w:35%"></span></td><td class="fl"><span><i></i><i></i><i></i><i class="o"></i><i class="o"></i><i class="o"></i><i class="o"></i><i class="y"></i><i class="o"></i><i class="o"></i><i></i><i></i></span></td><td class="nt"><svg><use href="#i-drop"/></svg><svg><use href="#i-leaf"/></svg></td></tr>
      <tr><td class="c"><b class="n o">20</b></td><td>Great Blue Lobelia</td><td class="sci">Lobelia siphilitica</td><td class="c"><b class="z o">1</b></td><td class="c">80–120</td><td class="dp"><span class="tr" style="--t:43%"></span><span class="fi" style="--l:46%;--w:13%"></span></td><td class="fl"><span><i></i><i></i><i></i><i class="l"></i><i class="l"></i><i class="l"></i><i class="l"></i><i class="l"></i><i class="l"></i><i class="l"></i><i class="l"></i><i></i></span></td><td class="nt"><svg><use href="#i-drop"/></svg><svg><use href="#i-frog"/></svg></td></tr>
    </tbody>
  </table>
  <div class="scroll"></div>

  <!-- 5. Flowering arch -->
  <h2 class="sec-title" style="left:449px;top:443px">5. Flowering Arch &amp; Seasonal Interest</h2>
  <svg class="arch" width="338" height="178" viewBox="0 0 380 200" font-family="Poppins,sans-serif">
    <g fill="none" stroke-linecap="butt">
      <path d="M40 195A150 150 0 0 1 340 195" stroke="#e7ecf0" stroke-width="16"/>
      <path d="M58 195A132 132 0 0 1 322 195" stroke="#eef2f4" stroke-width="10"/>
      <path d="M58 195A132 132 0 0 1 322 195" pathLength="12" stroke="#5faa3c" stroke-width="10" stroke-dasharray="0 1.6 8.4 12"/>
      <path d="M70 195A120 120 0 0 1 310 195" stroke="#f4f4f1" stroke-width="9"/>
      <path d="M70 195A120 120 0 0 1 310 195" pathLength="12" stroke="#f2c417" stroke-width="9" stroke-dasharray="0 2.8 6.8 12"/>
      <path d="M82 195A108 108 0 0 1 298 195" pathLength="12" stroke="#e0a45a" stroke-width="9" stroke-dasharray="0 1.4 8.2 12"/>
      <path d="M94 195A96 96 0 0 1 286 195" pathLength="12" stroke="#9b55c2" stroke-width="9" stroke-dasharray="0 4.4 4.2 12"/>
      <path d="M106 195A84 84 0 0 1 274 195" pathLength="12" stroke="#8fc2ee" stroke-width="9" stroke-dasharray="0 2.2 1.2 12"/>
      <path d="M106 195A84 84 0 0 1 274 195" pathLength="12" stroke="#f4f0e6" stroke-width="9" stroke-dasharray="0 3.6 5 12"/>
    </g>
    <g font-size="8" fill="#1b2530" text-anchor="middle">
      <text transform="translate(26.4 173.5) rotate(-82.5)">JAN</text>
      <text transform="translate(37.6 131.9) rotate(-67.5)">FEB</text>
      <text transform="translate(59.1 94.5) rotate(-52.5)">MAR</text>
      <text transform="translate(89.5 64.1) rotate(-37.5)">APR</text>
      <text transform="translate(126.9 42.6) rotate(-22.5)">MAY</text>
      <text transform="translate(168.5 31.4) rotate(-7.5)">JUN</text>
      <text transform="translate(211.5 31.4) rotate(7.5)">JUL</text>
      <text transform="translate(253.1 42.6) rotate(22.5)">AUG</text>
      <text transform="translate(290.5 64.1) rotate(37.5)">SEP</text>
      <text transform="translate(320.9 94.5) rotate(52.5)">OCT</text>
      <text transform="translate(342.4 131.9) rotate(67.5)">NOV</text>
      <text transform="translate(353.6 173.5) rotate(82.5)">DEC</text>
    </g>
  </svg>
  <div class="ph" role="img" aria-label="Flowering iris and pond plants at the foot of the arch" style="left:452px;top:574px;width:62px;height:48px;border-radius:34px 34px 4px 4px;background:linear-gradient(180deg,rgba(255,255,255,0),#e9d46a 35%,#b99ad6 60%,#6f9a4c)"></div>
  <div class="ph" role="img" aria-label="Flowering purple spikes and grasses at the foot of the arch" style="left:708px;top:574px;width:60px;height:48px;border-radius:34px 34px 4px 4px;background:linear-gradient(180deg,rgba(255,255,255,0),#c6a2dc 35%,#e0a45a 65%,#6f9a4c)"></div>
  <div class="arch-legend">
    <div><i style="background:#5faa3c"></i>At the edge</div>
    <div><i style="background:#f2c417"></i>Floating plants</div>
    <div><i style="background:#3f8fdc"></i>Submerged plants</div>
    <div><i style="background:#e0a45a"></i>Grasses &amp; reeds</div>
    <div><i style="background:#9b55c2"></i>Seasonal interest</div>
  </div>
  <div class="seasons">
    <div class="season s1"><h5>SPRING</h5><p role="img" aria-label="Spring pond scene">New growth<br>Early blooms<br>Wildlife active</p></div>
    <div class="season s2"><h5>SUMMER</h5><p role="img" aria-label="Summer pond scene">Peak flowering<br>Shade &amp; cooling<br>High biodiversity</p></div>
    <div class="season s3"><h5>AUTUMN</h5><p role="img" aria-label="Autumn pond scene">Seed heads<br>Habitat &amp; food<br>Prepare for winter</p></div>
    <div class="season s4"><h5>WINTER</h5><p role="img" aria-label="Winter pond scene">Structure<br>Wildlife shelter<br>Rest &amp; recovery</p></div>
  </div>

  <!-- 6. Companion planting -->
  <h2 class="sec-title" style="left:830px;top:443px">6. Companion Planting</h2>
  <table class="ctable">
    <colgroup><col style="width:88px"><col><col><col><col><col></colgroup>
    <thead>
      <tr>
        <th class="plant">Plant</th>
        <th><div class="hd"><svg><use href="#i-bee"/></svg>Pollinator<br>Support</div></th>
        <th><div class="hd"><svg><use href="#i-shade"/></svg>Shades<br>Water</div></th>
        <th><div class="hd"><svg><use href="#i-leaf"/></svg>Nutrient<br>Synergy</div></th>
        <th><div class="hd"><svg><use href="#i-home"/></svg>Habitat<br>Value</div></th>
        <th><div class="hd"><svg><use href="#i-grass"/></svg>Competes<br>Algae</div></th>
      </tr>
    </thead>
    <tbody>
      <tr><td>Marsh Marigold</td><td><i class="dot d-g"></i></td><td><i class="dot d-b"></i></td><td><i class="dot d-o"></i></td><td><i class="dot d-br"></i></td><td><i class="dot d-r"></i></td></tr>
      <tr><td>Yellow Flag Iris</td><td><i class="dot d-g"></i></td><td><i class="dot d-b"></i></td><td><i class="dot d-ol"></i></td><td><i class="dot d-br"></i></td><td><i class="dot d-rp"></i></td></tr>
      <tr><td>Water Mint</td><td><i class="dot d-g"></i></td><td><i class="dot d-b"></i></td><td><i class="dot d-o"></i></td><td><i class="dot d-br"></i></td><td><i class="dot d-p"></i></td></tr>
      <tr><td>Purple Loosestrife</td><td><i class="dot d-g"></i></td><td><i class="dot d-b"></i></td><td><i class="dot d-o"></i></td><td><i class="dot d-br"></i></td><td></td></tr>
      <tr><td>Sweet Flag</td><td><i class="dot d-g"></i></td><td><i class="dot d-b"></i></td><td><i class="dot d-ol"></i></td><td><i class="dot d-brl"></i></td><td></td></tr>
      <tr><td>Water Lily</td><td><i class="dot d-g"></i></td><td><i class="dot d-b"></i></td><td><i class="dot d-o"></i></td><td><i class="dot d-br"></i></td><td><i class="dot d-r"></i></td></tr>
      <tr><td>Yellow Water Lily</td><td><i class="dot d-g"></i></td><td><i class="dot d-b"></i></td><td><i class="dot d-o"></i></td><td><i class="dot d-br"></i></td><td><i class="dot d-rl"></i></td></tr>
      <tr><td>Frogbit</td><td><i class="dot d-g"></i></td><td><i class="dot d-b"></i></td><td><i class="dot d-o"></i></td><td><i class="dot d-brl"></i></td><td><i class="dot d-r"></i></td></tr>
      <tr><td>Hornwort</td><td><i class="dot d-g"></i></td><td><i class="dot d-b"></i></td><td><i class="dot d-o"></i></td><td><i class="dot d-br"></i></td><td><i class="dot d-r"></i></td></tr>
      <tr><td>Water Milfoil</td><td><i class="dot d-g"></i></td><td><i class="dot d-b"></i></td><td><i class="dot d-ol"></i></td><td><i class="dot d-brl"></i></td><td><i class="dot d-r"></i></td></tr>
    </tbody>
  </table>

  <!-- How to use -->
  <div class="howto">
    <h3>HOW TO USE THIS TEMPLATE</h3>
    <p>Edit the text, replace images and adjust colors to create your own planting plan for ponds, rain gardens and more.</p>
  </div>
  <div class="step" style="left:232px">
    <svg viewBox="0 0 26 26"><path d="M13 22C8 20 4 16 5 9c4 1 7 4 8 9 1-5 4-8 8-9 1 7-3 11-8 13z" fill="#1f3f5f"/></svg>
    <span>Choose your plants<br>based on zone<br>and function</span>
  </div>
  <div class="rule-v" style="left:355px;top:716px;height:32px"></div>
  <div class="step" style="left:375px">
    <svg viewBox="0 0 26 26" fill="none" stroke="#5da6dc" stroke-width="1.2"><path d="M13 4v18M8 8v14M18 8v14"/><circle cx="13" cy="6" r="1.5"/><circle cx="8" cy="10" r="1.5"/><circle cx="18" cy="10" r="1.5"/></svg>
    <span>Consider depth<br>and growth<br>conditions</span>
  </div>
  <div class="rule-v" style="left:505px;top:716px;height:32px"></div>
  <div class="step" style="left:520px">
    <svg viewBox="0 0 26 26"><path d="M13 3 7 12h4l-5 7h14l-5-7h4z" fill="#1f3f5f"/><rect x="12" y="19" width="2" height="4" fill="#1f3f5f"/></svg>
    <span>Combine species<br>for strong ecological<br>relationships</span>
  </div>
  <div class="rule-v" style="left:655px;top:716px;height:32px"></div>
  <div class="step" style="left:672px">
    <svg viewBox="0 0 26 26"><use href="#i-bee"/></svg>
    <span>Support wildlife and<br>create a natural<br>balance</span>
  </div>

  <!-- Legend -->
  <div class="legend">
    <h3>LEGEND ICONS</h3>
    <div class="legend-row">
      <div><svg><use href="#i-bee"/></svg>Pollinator<br>friendly</div>
      <div><svg><use href="#i-bird"/></svg>Wildlife<br>habitat</div>
      <div><svg><use href="#i-drop"/></svg>Improves<br>water quality</div>
      <div><svg><use href="#i-frog"/></svg>Good for<br>frogs</div>
      <div><svg><use href="#i-bird"/></svg>Attracts<br>birds</div>
      <div><svg><use href="#i-shade"/></svg>Good for<br>insects</div>
    </div>
  </div>

  <!-- Footer -->
  <footer class="footer">
    <span>© Verdant Institute</span>
    <span class="web">www.verdantinstitute.nl</span>
    <span>1 of 1</span>
  </footer>
</div>
</body>
</html>
```